Birchway Cleaning Commercial Flyer

Would like a flyer that will be used for making sales calls for commercial clients. These flyers will be handed out to Business Owners and facility managers. The flyer must peak interest, introduce the company, and give some information about our services. Birchway Cleaning Services (BWS) is a modern company that is eco-friendly. I have added what the uniform shirt looks like we have one in orange and one in blue. It would be nice to see the pictures you choose have the uniform on.

Target Market(s)

Office Mangers and Facility managers

Industry/Entity Type

Office Cleaning

Font styles to use
Serif

Colors
f78f20
0355a3
abd037

Requirements
Must have
• Modern clean look and feel. The flyer must straight forward and not busy.
• Have sections where bullet points or other written information can be placed
• Must be able to add and move information myself after the design has been decided on.
• Have a section that says:
• To learn more call 301-555-0148 or email info@birchway-tidyco.example
Nice to have
• Some pictures, clean and modern. Peak interest. The uniform to be photoshopped onto the models of the pictures
Should not have
• too busy

```html
<!DOCTYPE html>
<html lang="en">
<head>
<meta charset="utf-8">
<title>Birchway Cleaning Commercial Flyer</title>
<link rel="stylesheet" href="https://fonts.googleapis.com/css2?family=Open+Sans:ital,wght@0,400;0,600;1,400&display=swap">
<style>
  :root {
    --brand-blue: #0a6fbd;
    --deep-blue: #0355a3;
    --leaf-green: #8cc63f;
    --brand-orange: #f78f20;
    --text-grey: #444a50;
    --intro-grey: #555b61;
    --paper: #ffffff;
    --sky: #e3f1fa;
    --photo-tone: #d9cfc4;
    --inset-tone: #b59a6a;
  }
  * { margin: 0; padding: 0; box-sizing: border-box; }
  html, body { width: 898px; height: 1200px; overflow: hidden; }
  body {
    font-family: "Open Sans", Arial, sans-serif;
    background: linear-gradient(180deg, var(--sky) 0%, var(--paper) 22%, var(--paper) 70%, #f3f6f8 100%);
    position: relative;
    color: var(--text-grey);
  }
  .brand {
    position: absolute; left: 40px; top: 40px; width: 300px;
    display: flex; flex-direction: column; align-items: center;
  }
  .brand-mark {
    width: 92px; height: 92px; border-radius: 50%;
    background: var(--brand-orange);
  }
  .brand-name {
    margin-top: 14px;
    font-size: 25px; font-weight: 600; color: var(--deep-blue);
    white-space: nowrap;
  }
  .tagline {
    position: absolute; left: 440px; top: 42px; width: 400px;
    text-align: center; font-style: italic;
    font-size: 31px; line-height: 40px; color: var(--brand-blue);
  }
  .hero { position: absolute; left: 0; top: 140px; width: 898px; height: 520px; }
  .content { position: absolute; left: 39px; top: 650px; width: 800px; }
  .section-title {
    font-size: 38px; font-weight: 400; color: var(--brand-blue); line-height: 46px;
  }
  .intro {
    margin-top: 10px; width: 770px;
    font-style: italic; font-size: 19.5px; line-height: 28px; color: var(--intro-grey);
  }
  .assurances { margin-top: 14px; width: 730px; font-size: 15.5px; line-height: 22.5px; }
  .assurances ul { list-style: none; }
  .assurances li { padding-left: 9px; text-indent: -9px; }
  .assurances li::before { content: "· "; }
  .services-title {
    margin-top: 26px; margin-left: 5px;
    font-size: 20.5px; font-weight: 400; color: var(--brand-blue);
  }
  .services {
    margin-top: 14px; margin-left: 36px;
    display: grid; grid-template-columns: 348px 320px;
    list-style: none; font-size: 17px; line-height: 24.5px;
    grid-auto-flow: column; grid-template-rows: repeat(5, auto);
  }
  .services li { display: flex; align-items: center; gap: 8px; }
  .services svg { width: 15px; height: 15px; flex: none; }
  .contact-band { position: absolute; left: 0; top: 1060px; width: 898px; height: 140px; }
  .contact {
    position: absolute; left: 0; top: 1123px; width: 898px;
    text-align: center; color: #fff; font-size: 22.5px; line-height: 30px;
  }
</style>
</head>
<body>

<header>
  <div class="brand">
    <div class="brand-mark"></div>
    <div class="brand-name">Birchway Cleaning Services</div>
  </div>
  <p class="tagline">Trusted choice for<br>Office Cleaning Services</p>
</header>

<svg class="hero" viewBox="0 140 898 520">
  <path role="img" aria-label="Photo of a bright modern open-plan office with desks and potted plants"
        fill="var(--photo-tone)"
        d="M0 210 C140 240 300 250 470 215 C620 186 760 190 898 250 L898 595 C770 555 640 565 520 585 C380 608 240 615 120 585 C70 572 30 555 0 540 Z"/>
  <path fill="var(--brand-blue)" d="M0 192 C150 225 300 232 470 200 C630 170 770 170 898 228 L898 250 C760 190 620 186 470 215 C300 250 140 240 0 210 Z"/>
  <path fill="var(--leaf-green)" d="M390 190 C560 150 720 140 898 205 L898 245 C800 190 660 175 500 195 Z"/>
  <path fill="var(--brand-blue)" d="M520 585 C640 565 770 555 898 595 L898 625 C790 590 680 590 560 600 Z"/>
  <path fill="var(--leaf-green)" d="M0 540 C30 555 70 572 120 585 C240 615 380 608 530 590 C420 630 260 655 120 625 C60 612 20 590 0 578 Z"/>
  <circle role="img" aria-label="Photo of a janitorial cleaning cart" cx="710" cy="532" r="78" fill="var(--inset-tone)"/>
</svg>

<main class="content">
  <h1 class="section-title">Office Cleaning</h1>
  <p class="intro">If you're looking for a quality office cleaning company, then you've found the right partner in Birchway Cleaning Service.</p>
  <div class="assurances">
    <p>By employing our office cleaning services, you're assured of:</p>
    <ul>
      <li>A consistently high standard of office cleaning and customer service</li>
      <li>A fully trained and highly motivated cleaning team that all come with full police clearances.</li>
      <li>A comprehensive health and safety program that ensures the security and well being of both clients and staff.</li>
    </ul>
  </div>
  <h2 class="services-title">Our office cleaning service includes:</h2>
  <ul class="services">
    <li><svg viewBox="0 0 16 16"><path fill="#8cc63f" d="M2 14 C2 6 7 2 14 2 C14 9 10 14 2 14 Z"/><path stroke="#fff" stroke-width="1.2" fill="none" d="M4 12 L11 5"/></svg>Rubbish Removal</li>
    <li><svg viewBox="0 0 16 16"><path fill="#8cc63f" d="M2 14 C2 6 7 2 14 2 C14 9 10 14 2 14 Z"/><path stroke="#fff" stroke-width="1.2" fill="none" d="M4 12 L11 5"/></svg>Dusting</li>
    <li><svg viewBox="0 0 16 16"><path fill="#8cc63f" d="M2 14 C2 6 7 2 14 2 C14 9 10 14 2 14 Z"/><path stroke="#fff" stroke-width="1.2" fill="none" d="M4 12 L11 5"/></svg>Desk Cleaning</li>
    <li><svg viewBox="0 0 16 16"><path fill="#8cc63f" d="M2 14 C2 6 7 2 14 2 C14 9 10 14 2 14 Z"/><path stroke="#fff" stroke-width="1.2" fill="none" d="M4 12 L11 5"/></svg>Vacuuming &amp; Carpet Cleaning</li>
    <li><svg viewBox="0 0 16 16"><path fill="#8cc63f" d="M2 14 C2 6 7 2 14 2 C14 9 10 14 2 14 Z"/><path stroke="#fff" stroke-width="1.2" fill="none" d="M4 12 L11 5"/></svg>Disinfecting</li>
    <li><svg viewBox="0 0 16 16"><path fill="#8cc63f" d="M2 14 C2 6 7 2 14 2 C14 9 10 14 2 14 Z"/><path stroke="#fff" stroke-width="1.2" fill="none" d="M4 12 L11 5"/></svg>Mopping</li>
    <li><svg viewBox="0 0 16 16"><path fill="#8cc63f" d="M2 14 C2 6 7 2 14 2 C14 9 10 14 2 14 Z"/><path stroke="#fff" stroke-width="1.2" fill="none" d="M4 12 L11 5"/></svg>Lunchroom cleaning</li>
    <li><svg viewBox="0 0 16 16"><path fill="#8cc63f" d="M2 14 C2 6 7 2 14 2 C14 9 10 14 2 14 Z"/><path stroke="#fff" stroke-width="1.2" fill="none" d="M4 12 L11 5"/></svg>Hard Floor Stripping &amp; Sealing</li>
    <li><svg viewBox="0 0 16 16"><path fill="#8cc63f" d="M2 14 C2 6 7 2 14 2 C14 9 10 14 2 14 Z"/><path stroke="#fff" stroke-width="1.2" fill="none" d="M4 12 L11 5"/></svg>Window Cleaning</li>
    <li><svg viewBox="0 0 16 16"><path fill="#8cc63f" d="M2 14 C2 6 7 2 14 2 C14 9 10 14 2 14 Z"/><path stroke="#fff" stroke-width="1.2" fill="none" d="M4 12 L11 5"/></svg>Pressure Cleaning</li>
  </ul>
</main>

<footer>
  <svg class="contact-band" viewBox="0 1060 898 140" aria-hidden="true">
    <defs>
      <linearGradient id="bandTone" x1="0" y1="0" x2="1" y2="0">
        <stop offset="0" stop-color="#0a6fbd"/>
        <stop offset="0.5" stop-color="#1b84cc"/>
        <stop offset="1" stop-color="#0a6fbd"/>
      </linearGradient>
    </defs>
    <path fill="var(--leaf-green)" d="M0 1077 C300 1115 600 1110 898 1065 L898 1072 C600 1116 300 1120 0 1083 Z"/>
    <path fill="url(#bandTone)" d="M0 1083 C300 1120 600 1116 898 1072 L898 1200 L0 1200 Z"/>
  </svg>
  <p class="contact">To learn more call 301-555-0148<br>or email info@birchway-tidyco.example</p>
</footer>

</body>
</html>
```